Falcrest security business card

Looking for a business card for my security company

Target Market(s)

Security

Industry/Entity Type

Security

Contact Information for Business Card

Name - Gil Marston. Title - General manager - direct 314 862.4490 website www. falcrestsecurityservices.example email - gil@ falcrestsecurityservices.example

Requirements
Must have
• Logo attached

```html
<!DOCTYPE html>
<html lang="en">
<head>
<meta charset="utf-8">
<title>Falcrest Security Business Card</title>
<link href="https://fonts.googleapis.com/css2?family=Montserrat:wght@700&family=Open+Sans:wght@400;600&display=swap" rel="stylesheet">
<style>
  :root {
    --backdrop: #c9c9c9;
    --card-black: #1c1b1b;
    --gold: #d19a3a;
    --gold-light: #f3dda0;
    --gold-deep: #b47e2a;
    --ink: #141414;
    --text-light: #e8e8e8;
  }
  html, body {
    margin: 0;
    padding: 0;
    width: 1200px;
    height: 800px;
    overflow: hidden;
  }
  body {
    background: radial-gradient(ellipse at 40% 30%, #e6e6e6 0%, var(--backdrop) 70%, #b4b4b4 100%);
    position: relative;
    font-family: "Open Sans", sans-serif;
  }
  .card {
    position: absolute;
    width: 540px;
    height: 310px;
    border-radius: 22px;
    box-shadow: 0 14px 30px rgba(0,0,0,0.28);
    overflow: hidden;
  }
  .card--back {
    left: 50px;
    top: 110px;
    background: var(--card-black);
  }
  .card--front {
    left: 610px;
    top: 380px;
    background: radial-gradient(ellipse at 45% 45%, var(--gold-light) 0%, #e2bb6c 40%, var(--gold) 70%, var(--gold-deep) 100%);
  }
  .wordmark {
    position: absolute;
    display: flex;
    align-items: center;
    gap: 12px;
    font-family: "Montserrat", sans-serif;
    font-weight: 700;
    letter-spacing: 1px;
    text-transform: uppercase;
    line-height: 1;
  }
  .wordmark__square {
    display: block;
    width: 22px;
    height: 22px;
  }
  .card--back .wordmark {
    left: 38px;
    top: 138px;
    font-size: 38px;
    color: var(--gold);
  }
  .card--back .wordmark__square { background: var(--gold); }
  .card--front .wordmark {
    left: 50%;
    top: 50%;
    transform: translate(-50%, -50%);
    font-size: 58px;
    color: var(--ink);
  }
  .card--front .wordmark__square { background: var(--ink); width: 30px; height: 30px; }
  .contact {
    position: absolute;
    left: 296px;
    top: 96px;
    color: var(--text-light);
  }
  .contact__name {
    margin: 0;
    font-family: "Montserrat", sans-serif;
    font-weight: 700;
    font-size: 21px;
    color: var(--gold);
    text-transform: uppercase;
    letter-spacing: 0.5px;
  }
  .contact__title {
    margin: 2px 0 12px;
    font-size: 12px;
  }
  .contact__list {
    list-style: none;
    margin: 0;
    padding: 0;
    font-size: 11px;
  }
  .contact__item {
    display: flex;
    align-items: center;
    gap: 7px;
    margin-bottom: 5px;
  }
  .contact__icon {
    width: 10px;
    height: 10px;
    flex: none;
  }
</style>
</head>
<body>
  <section class="card card--back" aria-label="Card back with contact details">
    <div class="wordmark"><span class="wordmark__square"></span>Falcrest</div>
    <div class="contact">
      <p class="contact__name">Gil Marston</p>
      <p class="contact__title">General manager</p>
      <ul class="contact__list">
        <li class="contact__item">
          <svg class="contact__icon" viewBox="0 0 10 10"><path d="M2 0.5 L3.8 2.5 L2.8 3.6 Q4 6 6.4 7.2 L7.5 6.2 L9.5 8 L8.3 9.5 Q1 8 0.5 1.7 Z" fill="#d19a3a"/></svg>
          314 862.4490
        </li>
        <li class="contact__item">
          <svg class="contact__icon" viewBox="0 0 10 10"><rect x="0.5" y="2" width="9" height="6.5" fill="#d19a3a"/><path d="M0.5 2 L5 5.5 L9.5 2" stroke="#1c1b1b" stroke-width="0.9" fill="none"/></svg>
          gil@falcrestsecurityservices.example
        </li>
        <li class="contact__item">
          <svg class="contact__icon" viewBox="0 0 10 10"><circle cx="5" cy="5" r="4.5" fill="#d19a3a"/><path d="M0.5 5 H9.5 M5 0.5 Q2.5 5 5 9.5 M5 0.5 Q7.5 5 5 9.5" stroke="#1c1b1b" stroke-width="0.7" fill="none"/></svg>
          falcrestsecurityservices.example
        </li>
      </ul>
    </div>
  </section>

  <section class="card card--front" aria-label="Card front with company name">
    <div class="wordmark"><span class="wordmark__square"></span>Falcrest</div>
  </section>
</body>
</html>
```